QLM Stationery Design Project

Dear Designers,
We need a new stationery design for company to match our new logo.
Designers should provide a design for the following:
1. Business Card: 3.5x2 Inches.
2. Letterhead: A4 size.
3. Envelops: 25x35.5 Cm.
You can keep the Arabic name at the bottom of the logo Or you can use the separate attached Arabic Name.
Please refer to the attached logo guide for design information.
Sample Business Card information:
Name: Tariq Saleem
Position: Operation Manager
Tel: +966 920004717 Ex. 500
Fax: +966 (3)8462153
Mob: +966 (5)00387260
email: tariq@qlm-example.com.sa
URL: www.qlm-example.com.sa
Address:
Le Verger Tower, Suite 517
Nasser bin Omar Str.
Khobar, 34861
Saudi Arabia
Updates
Dear All,
Please note, we had uploaded our logo along with Arabic writing in Adobe illustrator format (.ai).
Regards,
Yousef
Dear All,
A sample data for the business card had been added as per your request.
Regards,
Yousef

```html
<!DOCTYPE html>
<html lang="en">
<head>
<meta charset="utf-8">
<title>QLM Business Card</title>
<link href="https://fonts.googleapis.com/css2?family=Open+Sans:wght@400;600;700&display=swap" rel="stylesheet">
<style>
  :root {
    --navy: #022b52;
    --grey: #9d9d9d;
    --text: #3a3a3a;
    --paper: #ffffff;
    --paper-shade: #ececec;
    --backdrop: #d6dee4;
    --line: #6f6f6f;
  }
  html, body {
    margin: 0;
    padding: 0;
    overflow: hidden;
  }
  .stage {
    position: relative;
    width: 1200px;
    height: 965px;
    background: var(--backdrop);
    font-family: "Open Sans", Arial, sans-serif;
    overflow: hidden;
  }
  .card {
    position: absolute;
    width: 645px;
    height: 369px;
    overflow: hidden;
  }
  /* Front */
  .card-front {
    left: 275px;
    top: 88px;
    background: var(--navy);
    color: #fff;
  }
  .card-front .brand-name {
    position: absolute;
    left: 0;
    right: 0;
    top: 118px;
    text-align: center;
    font-size: 96px;
    font-weight: 700;
    line-height: 1;
    letter-spacing: 4px;
    color: #fff;
  }
  .card-front .website {
    position: absolute;
    left: 0;
    right: 0;
    top: 320px;
    text-align: center;
    font-size: 14px;
    color: #fff;
  }
  /* Back */
  .card-back {
    left: 280px;
    top: 508px;
    background: linear-gradient(100deg, var(--paper) 45%, var(--paper-shade) 100%);
    color: var(--text);
  }
  .card-back .brand-name {
    position: absolute;
    left: 46px;
    top: 42px;
    font-size: 64px;
    font-weight: 700;
    line-height: 1;
    letter-spacing: 3px;
    color: var(--navy);
  }
  .person {
    position: absolute;
    left: 380px;
    top: 155px;
    width: 265px;
  }
  .person-name {
    margin: 0;
    font-size: 21px;
    font-weight: 700;
    color: var(--navy);
    line-height: 1.2;
  }
  .person-title {
    margin: 2px 0 0;
    font-size: 15px;
    color: var(--text);
  }
  .divider {
    height: 1px;
    background: var(--line);
    margin-top: 10px;
  }
  .contacts {
    position: absolute;
    left: 386px;
    top: 233px;
    margin: 0;
    padding: 0;
    list-style: none;
    font-size: 14.5px;
    line-height: 21.6px;
  }
  .contacts li {
    display: flex;
    align-items: center;
    gap: 8px;
  }
  .contacts svg {
    width: 16px;
    height: 16px;
    fill: var(--navy);
    flex: none;
  }
  .address {
    position: absolute;
    left: 46px;
    top: 255px;
    margin: 0;
    font-style: normal;
    font-size: 14.5px;
    line-height: 21.6px;
  }
  .footer-band {
    position: absolute;
    left: 0;
    right: 0;
    bottom: 0;
    height: 18px;
    background: var(--navy);
  }
  .web-tab {
    position: absolute;
    left: 344px;
    bottom: 0;
    width: 270px;
    height: 37px;
  }
  .web-tab svg {
    position: absolute;
    inset: 0;
  }
  .web-tab span {
    position: relative;
    display: block;
    text-align: center;
    line-height: 34px;
    font-size: 14.5px;
    color: #fff;
  }
</style>
</head>
<body>
<div class="stage">

  <section class="card card-front">
    <div class="brand-name">QLM</div>
    <div class="website">www.qlm-example.com.sa</div>
  </section>

  <section class="card card-back">
    <div class="brand-name">QLM</div>

    <div class="person">
      <h1 class="person-name">Tariq Saleem</h1>
      <p class="person-title">Operation Manager</p>
      <div class="divider"></div>
    </div>

    <ul class="contacts">
      <li>
        <svg viewBox="0 0 16 16" aria-hidden="true"><path d="M4 1l2.5 3-1.5 1.5c.8 2 2.5 3.7 4.5 4.5L11 8.5l3 2.5-1.5 3C7 14 2 9 2 2.5z"/></svg>
        +966 920004717 Ex. 500
      </li>
      <li>
        <svg viewBox="0 0 16 16" aria-hidden="true"><path d="M4 1h6v4H4zM2 6h12v8H2zm2 2v1h2V8zm3 0v1h2V8zm3 0v1h2V8zM4 11v1h8v-1z"/></svg>
        +966 (3)8462153
      </li>
      <li>
        <svg viewBox="0 0 16 16" aria-hidden="true"><path d="M4 0h8a1 1 0 011 1v14a1 1 0 01-1 1H4a1 1 0 01-1-1V1a1 1 0 011-1zm1 2v10h6V2zm3 11a1 1 0 100 2 1 1 0 000-2z"/></svg>
        +966 (5)00387260
      </li>
      <li>
        <svg viewBox="0 0 16 16" aria-hidden="true"><path d="M1 3h14v10H1zm1.5 1.2L8 8.5l5.5-4.3V12h-11z"/></svg>
        tariq@qlm-example.com.sa
      </li>
    </ul>

    <address class="address">
      Le Verger Tower, Suite 517<br>
      Nasser bin Omar Str. Khobar<br>
      34861, Saudi Arabia
    </address>

    <div class="footer-band"></div>
    <div class="web-tab">
      <svg viewBox="0 0 270 37" preserveAspectRatio="none" aria-hidden="true">
        <path d="M0 37 L10 8 Q13 0 22 0 L248 0 Q257 0 260 8 L270 37 Z" fill="#9d9d9d"/>
      </svg>
      <span>www.qlm-example.com.sa</span>
    </div>
  </section>

</div>
</body>
</html>
```